Stylish new business card needed!

Hello everyone! I am in need of a new business card design for an alarm company here in Hurricane WV. I have all fonts, color codes and logos provided for you use! We are a young company and like the style of a clean sleek looking business card. Would like it double sided, one side holding the logo and the other with your design!
Target Market(s)
The people that are looking for the newest tech for home automation and security
Industry/Entity Type
Alarm services; Home automation
Contact Information for Business Card
Name of person; position (Sales; Installer); Phone Number (555.419.7362); Employee cell Number; Website (www.GuardedByVelm.example); Employee Email; Double sided
Look and feel
Each slider illustrates characteristics of the customer's brand and the style your logo design should communicate.

```html
<!DOCTYPE html>
<html lang="en">
<head>
<meta charset="utf-8">
<title>Guarded by Velm — Business Card</title>
<link href="https://fonts.googleapis.com/css2?family=Arimo:wght@400;700&family=Archivo+Black&display=swap" rel="stylesheet">
<style>
  :root {
    --bg: #0e0e0f;
    --card: #2a2a2b;
    --card-light: #2e2e2f;
    --orange: #f47a35;
    --white: #f4f4f4;
    --emboss: #4a4a4c;
  }
  html, body {
    margin: 0;
    width: 1200px;
    height: 963px;
    overflow: hidden;
    background: var(--bg);
  }
  .stage {
    width: 1200px;
    height: 963px;
    display: flex;
    flex-direction: column;
    align-items: center;
    justify-content: center;
    gap: 48px;
  }
  .card {
    position: relative;
    flex: none;
    width: 640px;
    height: 366px;
    background: radial-gradient(circle at 55% 45%, var(--card-light) 0%, var(--card) 60%);
    border-radius: 20px;
    box-shadow: 0 4px 0 var(--orange), 0 18px 36px rgba(0,0,0,.6);
    font-family: "Arimo", Arial, sans-serif;
    color: var(--white);
    overflow: hidden;
  }

  /* Front */
  .brand {
    position: absolute;
    left: 46px;
    top: 44px;
  }
  .brand-row {
    display: flex;
    align-items: center;
    gap: 12px;
  }
  .brand-mark {
    width: 24px;
    height: 24px;
    border-radius: 50%;
    background: var(--orange);
  }
  .brand-name {
    font-family: "Archivo Black", "Arial Black", sans-serif;
    font-size: 30px;
    letter-spacing: .5px;
    color: var(--white);
    text-transform: uppercase;
    line-height: 1;
  }
  .brand-tagline {
    margin-top: 9px;
    font-family: "Archivo Black", "Arial Black", sans-serif;
    font-size: 9px;
    letter-spacing: 1px;
    color: var(--orange);
    text-transform: uppercase;
  }
  .contact {
    position: absolute;
    left: 340px;
    top: 168px;
  }
  .person-name {
    font-family: "Archivo Black", "Arial Black", sans-serif;
    font-size: 21px;
    font-weight: 400;
    color: var(--orange);
    text-transform: uppercase;
    letter-spacing: .4px;
    line-height: 1.1;
    margin: 0;
  }
  .person-role {
    font-size: 16px;
    line-height: 1.2;
    margin: 3px 0 12px;
  }
  .icons {
    display: flex;
    gap: 9px;
    margin-bottom: 12px;
  }
  .icons svg { width: 22px; height: 22px; }
  .details {
    list-style: none;
    padding: 0;
    margin: 0;
    font-size: 16px;
    line-height: 1.4;
  }

  /* Back */
  .back-brand {
    position: absolute;
    right: 70px;
    top: 50%;
    transform: translateY(-50%);
    display: flex;
    align-items: center;
    gap: 20px;
  }
  .back-mark {
    width: 56px;
    height: 56px;
    border-radius: 50%;
    background: var(--orange);
  }
  .back-name {
    font-family: "Archivo Black", "Arial Black", sans-serif;
    font-size: 72px;
    line-height: 1;
    letter-spacing: 2px;
    color: var(--emboss);
    text-transform: uppercase;
  }
</style>
</head>
<body>
<main class="stage">
  <section class="card card-front" aria-label="Card front">
    <div class="brand">
      <div class="brand-row">
        <span class="brand-mark"></span>
        <span class="brand-name">Guarded by Velm</span>
      </div>
      <div class="brand-tagline">Automation and Security Services</div>
    </div>

    <div class="contact">
      <h1 class="person-name">Marcus Hale</h1>
      <p class="person-role">Sales / Installer</p>
      <div class="icons">
        <svg viewBox="0 0 30 30" aria-label="Phone">
          <circle cx="15" cy="15" r="13" fill="none" stroke="var(--orange)" stroke-width="2"/>
          <path d="M10 9c0 6 5 11 11 11l1-3-3-1-1.5 1.5c-2-1-3.5-2.5-4.5-4.5L14.5 12l-1-3z" fill="var(--orange)"/>
        </svg>
        <svg viewBox="0 0 30 30" aria-label="Email">
          <circle cx="15" cy="15" r="13" fill="none" stroke="var(--orange)" stroke-width="2"/>
          <rect x="8.5" y="10" width="13" height="10" fill="none" stroke="var(--orange)" stroke-width="1.6"/>
          <path d="M8.5 10l6.5 5.5 6.5-5.5" fill="none" stroke="var(--orange)" stroke-width="1.6"/>
        </svg>
        <svg viewBox="0 0 30 30" aria-label="Website">
          <circle cx="15" cy="15" r="13" fill="none" stroke="var(--orange)" stroke-width="2"/>
          <circle cx="15" cy="15" r="7" fill="none" stroke="var(--orange)" stroke-width="1.5"/>
          <ellipse cx="15" cy="15" rx="3" ry="7" fill="none" stroke="var(--orange)" stroke-width="1.3"/>
          <path d="M8 15h14M9 11.5h12M9 18.5h12" stroke="var(--orange)" stroke-width="1.2"/>
        </svg>
      </div>
      <ul class="details">
        <li>555.419.7362</li>
        <li>info@GuardedByVelm.example</li>
        <li>www.GuardedByVelm.example</li>
      </ul>
    </div>
  </section>

  <section class="card card-back" aria-label="Card back">
    <div class="back-brand">
      <span class="back-mark"></span>
      <span class="back-name">Velm</span>
    </div>
  </section>
</main>
</body>
</html>
```